Brocure for Brindlo - Social Media Management

Brindlo is a Dutch company in the market of Social Media growth. We need a brochure (digital/PDF) for our company. Please see attached word doc for the text and attached logo. The initial proposal can contain just the first 4 pages text of the word doc.

We use informal language in all our communication.

Slogan: Effectieve Social Media Marketing voor professionals en ondernemers

Website: brindlopq.nl

Industry/Entity Type

Digital Marketing

Contact Information for Business Card

Contact details:

Joris ter Haaksel
joris@brindlopq.nl
06-47915328

```html
<!DOCTYPE html>
<html lang="nl">
<head>
<meta charset="utf-8">
<title>Brindlo brochure</title>
<link rel="stylesheet" href="https://fonts.googleapis.com/css2?family=Montserrat:wght@500;600;700;800&family=Open+Sans:wght@400;600;700&display=swap">
<style>
:root{
  --orange:#e2561a;
  --orange-light:#f08a4a;
  --orange-text:#ee5a1e;
  --navy:#1c3557;
  --band:#ececec;
  --paper:#fafafa;
  --stage:#dcdcde;
  --body:#4a4a4a;
  --white:#ffffff;
}
*{margin:0;padding:0;box-sizing:border-box}
html,body{width:1200px;height:2271px;overflow:hidden;background:var(--stage)}
body{position:relative;font-family:"Open Sans",sans-serif;color:var(--body)}
.spread{position:absolute;left:180px;width:840px;height:594px;display:flex;box-shadow:0 6px 18px rgba(0,0,0,.12)}
.spread--cover{top:81px}
.spread--inner-a{top:838px}
.spread--inner-b{top:1595px}
.page{position:relative;width:420px;height:594px;overflow:hidden;background:var(--paper)}
.page + .page{border-left:1px solid rgba(0,0,0,.08)}

/* cover */
.cover-back{background:var(--orange)}
.cover-back .faint-mark{position:absolute;left:130px;top:70px;width:200px;height:200px;border-radius:50%;border:22px solid rgba(150,40,0,.18)}
.cover-back .contact{position:absolute;left:48px;bottom:60px;color:var(--white)}
.brand{font-family:"Montserrat",sans-serif;font-weight:800;letter-spacing:1px;display:flex;align-items:center;gap:6px}
.brand .dot{width:14px;height:14px;border-radius:50%;border:2px solid currentColor}
.cover-back .brand{font-size:22px;color:var(--white);margin-bottom:26px}
.contact h3{font-family:"Montserrat",sans-serif;font-weight:700;font-size:15px;color:var(--navy);padding-bottom:6px;border-bottom:2px solid var(--white);width:90px;margin-bottom:16px}
.contact li{list-style:none;display:flex;align-items:center;gap:12px;font-family:"Montserrat",sans-serif;font-weight:600;font-size:13px;margin-bottom:10px}
.contact svg{width:16px;height:16px;fill:var(--navy)}
.cover-front{background:linear-gradient(160deg,var(--orange-light),var(--orange));color:var(--white);text-align:center}
.cover-front .brand{justify-content:center;font-size:24px;margin-top:60px}
.cover-front h1{font-family:"Montserrat",sans-serif;font-weight:800;font-size:36px;line-height:1.05;margin-top:22px}
.cover-front h1 .line-1{color:var(--white);display:block}
.cover-front h1 .line-2{color:var(--navy);display:block}
.cover-front .tagline{font-family:"Montserrat",sans-serif;font-size:12px;font-weight:500;margin-top:6px}
.cover-front .illustration{width:250px;height:250px;margin:26px auto 0;border-radius:50%;background:radial-gradient(circle,rgba(255,255,255,.55),rgba(255,255,255,.08) 70%)}
.cover-front .site{font-family:"Montserrat",sans-serif;font-weight:700;font-size:15px;letter-spacing:2px;margin-top:26px}

/* inner */
.inner{padding:26px 26px 0}
.inner h2{font-family:"Montserrat",sans-serif;font-weight:800;font-size:13px;color:var(--orange-text);line-height:1.25;margin-bottom:12px}
.block{padding:9px 26px;margin:0 -26px}
.block--band{background:var(--band)}
.block h4{font-family:"Montserrat",sans-serif;font-weight:700;font-size:10.5px;color:var(--navy);margin-bottom:4px}
.block p{font-size:7.4px;line-height:1.45;margin-bottom:3px}
.block p strong{color:#222}
.lead{font-size:8px;color:var(--orange-text);font-weight:600;margin-bottom:6px}
.platforms{display:grid;grid-template-columns:1.6fr 1fr;gap:5px 14px}
.platforms li{list-style:none;display:flex;align-items:center;gap:6px;font-size:7.2px;font-weight:700;color:#222}
.platforms .ico{flex:none;width:14px;height:14px;border-radius:50%;background:var(--navy)}
.ribbon{display:inline-block;background:var(--orange);color:var(--white);font-family:"Montserrat",sans-serif;font-weight:700;font-size:12px;padding:5px 18px;margin:4px 0 6px 60px;transform:rotate(-4deg)}
.photo{position:absolute;left:26px;right:26px;top:200px;height:300px;background:linear-gradient(135deg,#1b5fae,#2a86d6 55%,#174a8a)}

/* footer */
.footer{position:absolute;left:26px;right:26px;bottom:18px;height:26px;display:flex;align-items:center}
.footer .brand{font-size:10px;color:var(--orange)}
.footer .brand .dot{width:9px;height:9px}
.footer .rule{flex:1;height:1px;background:var(--navy);margin:0 8px}
.footer .pill{background:var(--navy);color:var(--white);font-family:"Montserrat",sans-serif;font-size:8px;font-weight:600;letter-spacing:1px;padding:4px 14px;border-radius:10px 0 0 10px}
.footer .num{width:22px;height:22px;border-radius:50%;background:var(--orange);color:var(--navy);font-family:"Montserrat",sans-serif;font-weight:800;font-size:8px;display:flex;align-items:center;justify-content:center;margin-left:-4px}
</style>
</head>
<body>

<section class="spread spread--cover">
  <div class="page cover-back">
    <div class="faint-mark"></div>
    <div class="contact">
      <div class="brand"><span class="dot"></span>BRINDLO</div>
      <h3>Contact us</h3>
      <ul>
        <li><svg viewBox="0 0 24 24"><path d="M6.6 10.8a15 15 0 006.6 6.6l2.2-2.2a1 1 0 011-.25 11.4 11.4 0 003.6.6 1 1 0 011 1V20a1 1 0 01-1 1A17 17 0 013 4a1 1 0 011-1h3.5a1 1 0 011 1 11.4 11.4 0 00.6 3.6 1 1 0 01-.25 1z"/></svg>06-47915328</li>
        <li><svg viewBox="0 0 24 24"><path d="M2 5h20v14H2zm2 2v.5l8 5 8-5V7z"/></svg>joris@brindlopq.nl</li>
        <li><svg viewBox="0 0 24 24"><circle cx="12" cy="12" r="10"/></svg>www.brindlopq.nl</li>
      </ul>
    </div>
  </div>
  <div class="page cover-front">
    <div class="brand"><span class="dot"></span>BRINDLO</div>
    <h1><span class="line-1">EFFECTIEVE</span><span class="line-2">SOCIAL MEDIA</span></h1>
    <p class="tagline">Marketing voor professionals en ondernemers</p>
    <div class="illustration" role="img" aria-label="Illustratie van een laptop met verbonden social media iconen"></div>
    <p class="site">www.brindlopq.nl</p>
  </div>
</section>

<section class="spread spread--inner-a">
  <div class="page inner">
    <h2>SOCIAL MEDIA MARKETING VOOR ZAKELIJKE PROFESSIONALS EN ONDERNEMERS</h2>
    <div class="block">
      <h4>Groei, interactie en content</h4>
      <p>Je bereik vergroten, traffic genereren en daarmee meer omzet behalen. Dat is wat wij beogen. Onze services helpen jou en je bedrijf om via sociale media te groeien. Met slimme content en gerichte interactie bouwen we aan een netwerk dat echt iets voor je doet.</p>
      <p><strong>(actieve interactie + relevante content) &gt; actieve volgers &gt; traffic + omzet</strong></p>
    </div>
    <div class="block block--band">
      <h4>Wie zijn wij?</h4>
      <p>Wij zijn Brindlo. Een team van social media experts dat je sociale netwerk activeert en het bereik vergroot. We zorgen voor sociale interactie met volgers, steeds met een heldere strategie. Zo genereren we traffic naar je website of shop.</p>
      <p><strong>Het doel? Meer omzet. Simpel en heel meetbaar.</strong></p>
    </div>
    <div class="block">
      <h4>Voor wie?</h4>
      <p>Onze dienstverlening kan ingezet worden op zowel persoonlijke zakelijke profielen (bijv. Proflink) of voor bedrijfspagina's op diverse sociale mediakanalen.</p>
    </div>
    <div class="block block--band">
      <h4>Wat doen we?</h4>
      <p>Samen met jou bepalen we je doelen in de sociale netwerken. Zowel strategisch als operationeel. Wij richten ons op de juiste doelgroep en zorgen voor een netwerk van actieve volgers.</p>
      <p>Voor zakelijke professionals verzorgen we persoonlijke branding en zetten we je neer als expert. Voor bedrijven versterken we de merkbekendheid en de online herkenbaarheid.</p>
      <p>Onze diensten voor bedrijven bestaan uit de wekelijkse creatie van content en interactie. We zorgen ervoor dat je merk zichtbaar blijft.</p>
    </div>
    <div class="footer"><span class="brand"><span class="dot"></span>BRINDLO</span><span class="rule"></span><span class="pill">www.brindlopq.nl</span><span class="num">01</span></div>
  </div>
  <div class="page inner">
    <div class="block block--band" style="margin-top:-26px;padding-top:26px">
      <h4>Welke platformen?</h4>
      <p class="lead">We bieden onze diensten aan op alle belangrijke platformen:</p>
      <ul class="platforms">
        <li><span class="ico"></span>Proflink (bedrijfspagina's en persoonlijke profielen)</li>
        <li><span class="ico"></span>Tjilp</li>
        <li><span class="ico"></span>Kringboek (bedrijfspagina's en groepen)</li>
        <li><span class="ico"></span>Vidkanaal</li>
        <li><span class="ico"></span>Snapverse (bedrijfspagina's en persoonlijke profielen)</li>
        <li><span class="ico"></span>Zoekmap Bedrijf</li>
        <li><span class="ico"></span>Optioneel: Clipster, Moodwall, Praatplein en Blogbox</li>
      </ul>
    </div>
    <div class="block">
      <h4>Waarom kies je voor ons?</h4>
      <p>Jij hebt jouw vak, wij het onze. Als iedereen doet waar hij goed in is, worden daar allemaal beter van. Wij zijn goed in het activeren en vergroten van je sociale netwerk. Daarvoor gebruiken we een slimme mix van kennis en tools.</p>
      <p>Een strategie die ervoor zorgt dat jij je kunt focussen op je corebusiness. Met als resultaat: meer traffic, meer leads en meer omzet.</p>
    </div>
    <div class="block block--band">
      <h4>Hoe lang gaan we met elkaar in zee?</h4>
      <p>Een groeistrategie werkt op de lange termijn het beste als die groei organisch is. Dat vraagt dus ook een strategie voor de lange termijn. Lang is relatief, maar je moet erop rekenen dat we minimaal een jaar nodig hebben om de strategie optimaal te laten werken. Natuurlijk is er in elke situatie snelle winst te behalen. Belangrijk is dat je elkaar leert kennen en begrijpen.</p>
    </div>
    <div class="block">
      <h4>Groeien op sociale media</h4>
      <p>Het staat als een paal boven water: sociale media zijn een krachtig marketinginstrument. Een kans die je niet voorbij kunt laten gaan. Het geeft je de kans om je merk op te bouwen, je zicht- en vindbaarheid te verbeteren en leads te genereren. Het beheren van je sociale platforms is een tijdrovende klus. Om resultaat te krijgen moet je het ook nog eens slim doen.</p>
    </div>
    <div class="footer"><span class="brand"><span class="dot"></span>BRINDLO</span><span class="rule"></span><span class="pill">www.brindlopq.nl</span><span class="num">02</span></div>
  </div>
</section>

<section class="spread spread--inner-b">
  <div class="page inner">
    <div class="block block--band" style="margin-top:-26px;padding-top:26px">
      <h4>Volledig social management</h4>
      <p>We bieden een compleet beheer van je sociale media waarmee je betrokkenheid van volgers realiseert en actief groeit. We combineren content, interactie en analyse tot een helder plan dat werkt.</p>
    </div>
    <div class="block">
      <h4>Volledig sociaal management</h4>
      <p>Je bent al een poos bezig met het beheren van je sociale media, maar ziet geen commercieel resultaat? Wij nemen het van je over en zetten een strategie neer die echt bijdraagt aan groei, leads en meer interactie met je doelgroep.</p>
    </div>
    <div class="block block--band">
      <h4>Groeistrategie</h4>
      <p>Je bent al een poos bezig en wilt de volgende stap zetten. Wij stellen een strategie op maat op en geven je de tools om deze zelf uit te voeren. Zo groeit je netwerk en je bereik op een gezonde manier.</p>
    </div>
    <span class="ribbon">Hoe werkt het?</span>
    <div class="block">
      <h4>Quick Scan&amp; advies</h4>
      <p>We starten altijd met een grondige analyse van je website en sociale kanalen. Op basis daarvan geven we je advies over de beste aanpak.</p>
    </div>
    <div class="block">
      <h4>Je wilt met ons in zee</h4>
      <p>Als je besluit met ons verder te gaan, dan maken we samen een plan. We bespreken je doelen en de kanalen die het beste bij je passen.</p>
    </div>
    <div class="block">
      <h4>Pakketkeuze</h4>
      <p>We hebben verschillende pakketten waaruit je kunt kiezen. Geen vaste kosten of lange verplichtingen, wel een heldere prijs per maand.</p>
    </div>
    <div class="footer"><span class="brand"><span class="dot"></span>BRINDLO</span><span class="rule"></span><span class="pill">www.brindlopq.nl</span><span class="num">03</span></div>
  </div>
  <div class="page inner">
    <div class="block">
      <h4>Implementatie</h4>
      <p>Natuurlijk wil je zo snel mogelijk resultaat zien. Dat willen wij ook. We werken de strategie uit in een plan en gaan voor jou aan het werk. Met de prioriteit op de gebieden die zo snel mogelijk resultaten opleveren. We richten daarvoor de benodigde systemen in en houden de vinger aan de pols.</p>
    </div>
    <div class="block">
      <h4>Terugkoppeling en verbetering</h4>
      <p>Iedere ondernemer is gedreven als het gaat om het behalen van resultaten. Zo ook wij. Wij doen er alles aan om onze dienstverlening zo succesvol mogelijk te laten zijn en jouw sociale doelen te behalen. We hebben regelmatig contact om de resultaten te bespreken en te verbeteren.</p>
    </div>
    <div class="photo" role="img" aria-label="Foto van gekleurde blokjes met social media iconen op een blauwe achtergrond"></div>
    <div class="footer"><span class="brand"><span class="dot"></span>BRINDLO</span><span class="rule"></span><span class="pill">www.brindlopq.nl</span><span class="num">04</span></div>
  </div>
</section>

</body>
</html>
```